A Maple Syrup Label for a Local Buniness

We are looking for a label for our maple syrup business. Our business currently sells honey, and we are expanding into maple syrup. Our Business name is "Brackley Honey" and we currently have a logo attached below. We would like to incorporate the bee and Brackley Honey part, but the label could also read "Brackley Farms" with the words maple syrup. We do not want consumers to confuse the maple syrup jars with the honey jars. It should be clear that the jars contain maple syrup. We are open to new designs as well.

```html
<!DOCTYPE html>
<html lang="en">
<head>
<meta charset="utf-8">
<title>Brackley Honey — Maple Syrup Label</title>
<link rel="stylesheet" href="https://fonts.googleapis.com/css2?family=Bebas+Neue&family=Libre+Baskerville&family=Oswald:wght@400&display=swap">
<style>
  :root {
    --page: #ecebec;
    --cream-warm: #f4dfc4;
    --cream-light: #f7efdf;
    --cream-cool: #eee5d3;
    --ink: #1b1a18;
    --gold: #f0b220;
    --gold-deep: #e6a516;
    --leaf: #f5d98f;
  }
  html, body {
    margin: 0;
    width: 1200px;
    height: 1200px;
    overflow: hidden;
    background: var(--page);
  }
  .label {
    position: absolute;
    left: 50px;
    top: 240px;
    width: 1100px;
    height: 720px;
    box-shadow: 0 10px 30px rgba(0,0,0,0.12);
  }
  .brand-name { font-family: "Oswald", sans-serif; font-weight: 400; fill: var(--ink); }
  .title { font-family: "Bebas Neue", sans-serif; fill: var(--ink); }
  .pure { font-family: "Oswald", sans-serif; font-weight: 400; fill: var(--ink); }
  .serif { font-family: "Libre Baskerville", serif; fill: var(--ink); }
  .badge-text { font-family: "Oswald", sans-serif; font-weight: 400; fill: var(--ink); }
  .rule { stroke: var(--ink); stroke-width: 2; }
</style>
</head>
<body>
<svg class="label" viewBox="0 0 1100 720" xmlns="http://www.w3.org/2000/svg">
  <defs>
    <linearGradient id="label-bg" x1="0" x2="1" y1="0" y2="0">
      <stop offset="0" stop-color="var(--cream-warm)"/>
      <stop offset="0.45" stop-color="var(--cream-light)"/>
      <stop offset="1" stop-color="var(--cream-cool)"/>
    </linearGradient>
    <radialGradient id="leaf-glow" cx="0.5" cy="0.55" r="0.5">
      <stop offset="0" stop-color="var(--leaf)" stop-opacity="0.7"/>
      <stop offset="0.7" stop-color="var(--leaf)" stop-opacity="0.4"/>
      <stop offset="1" stop-color="var(--leaf)" stop-opacity="0"/>
    </radialGradient>
    <path id="badge-top" d="M 698 532 A 89 89 0 0 1 876 532"/>
    <path id="badge-bottom" d="M 685 532 A 102 102 0 0 0 889 532"/>
  </defs>

  <rect class="label-base" width="1100" height="720" fill="url(#label-bg)"/>

  <ellipse class="leaf-backdrop" role="img" aria-label="Faint maple leaf behind the title" cx="573" cy="340" rx="390" ry="330" fill="url(#leaf-glow)"/>

  <g class="brand">
    <circle cx="420" cy="110" r="14" fill="var(--gold)"/>
    <text class="brand-name" x="448" y="126" font-size="44" letter-spacing="2">BRACKLEY HONEY</text>
  </g>

  <line class="rule" x1="165" y1="218" x2="947" y2="218"/>
  <text class="title" x="556" y="362" font-size="196" text-anchor="middle" textLength="770" lengthAdjust="spacingAndGlyphs">MAPLE SYRUP</text>
  <line class="rule" x1="165" y1="384" x2="947" y2="384"/>

  <text class="title" x="192" y="550" font-size="164" textLength="288" lengthAdjust="spacingAndGlyphs">100%</text>
  <text class="pure" font-size="60" letter-spacing="2" transform="translate(592 552) rotate(-90)">PURE</text>
  <line class="rule" x1="195" y1="578" x2="634" y2="578"/>
  <text class="serif" x="414" y="634" font-size="44" text-anchor="middle" letter-spacing="1">SMALL BATCH</text>
  <line class="rule" x1="195" y1="658" x2="634" y2="658"/>

  <g class="grade-badge">
    <circle cx="787" cy="532" r="110" fill="var(--gold)"/>
    <text class="badge-text" font-size="21" letter-spacing="1.5">
      <textPath href="#badge-top" startOffset="50%" text-anchor="middle">TAPPED STRAIGHT</textPath>
    </text>
    <text class="badge-text" x="787" y="524" font-size="37" text-anchor="middle">GRADE A</text>
    <text class="badge-text" x="787" y="566" font-size="37" text-anchor="middle">DARK ROBUST</text>
    <line x1="752" y1="590" x2="822" y2="590" stroke="var(--ink)" stroke-width="2"/>
    <text class="badge-text" font-size="21" letter-spacing="1.5">
      <textPath href="#badge-bottom" startOffset="50%" text-anchor="middle" dominant-baseline="hanging">FROM THE FARM</textPath>
    </text>
  </g>

  <rect class="band" x="0" y="664" width="1100" height="56" fill="var(--gold)"/>
  <rect class="band-edge" x="1040" y="664" width="60" height="56" fill="var(--gold-deep)"/>
</svg>
</body>
</html>
```